Business Card needed for International Migration and Education business

we are based in Australia, the business is called 'Brightpath Migration' and its sister business for international education is called 'Brightpath Studies' - we need the design for the business 'Brightpath Migration' - Brightpath Migration is about migration to Australia (but not limited to Australia only therefore purely Australian look would not fit). We would like to see designs that use the color blue or acqua and maybe orange..all those colours don't have to be used together and not only those colours are to be used. We are looking for a modern design. The final design should communicate modern thinking, professionalism, dynamism, confidence. We would like to use the same business card design for our sister business "Brightpath Studies" - which is business about studying in different countries as we recruit students to study in Australia, USA, New Zealand, Canada, UK etc. We would like to be able the final design to be easily changed by us to fit the 'Brightpath Studies' business - we would only change the contact text (email address etc)

The information to be included in the business card: Rosalind Tepperly Managing Director Migration Agent MARN 0719264 Brightpath Migration postal address: PO Box 2274, Fernvale South VIC 3195, Australia mobile: 0417296385 office address: Level 1, 287 Corran Street, Tullagrove VIC 3211 web www.brightpathmigration.example telephone: 61 3 8574 3162 fax + 61 3 8539 7041 email: rosalind@brightpathmigration.example

Industry/Entity Type

Education

```html
<!DOCTYPE html>
<html lang="en">
<head>
<meta charset="utf-8">
<title>Brightpath Migration and Brightpath Studies – Identity and Business Cards</title>
<link href="https://fonts.googleapis.com/css2?family=Arimo:wght@400;700&display=swap" rel="stylesheet">
<style>
  :root {
    --brand-blue: #1d5a9c;
    --brand-navy: #1c4a86;
    --ink: #111111;
    --rule: #2b5d98;
    --card-bg: #ffffff;
    --map-tone: #e3e6ee;
    --stage: #ece8e3;
    --mark-light: #4a9be0;
    --mark-dark: #15508f;
  }
  * { margin: 0; padding: 0; box-sizing: border-box; }
  html, body { width: 1200px; height: 1000px; overflow: hidden; background: #ffffff; }
  body { position: relative; font-family: "Arimo", Arial, sans-serif; color: var(--ink); }

  .brand-lockup { position: absolute; top: 128px; height: 170px; display: flex; align-items: center; }
  .brand-lockup--migration { left: 65px; }
  .brand-lockup--studies { left: 637px; }
  .brand-mark {
    width: 170px; height: 170px; border-radius: 50%;
    background: radial-gradient(circle at 35% 30%, var(--mark-light), var(--mark-dark));
    flex: none;
  }
  .brand-name {
    margin-left: 34px; font-weight: 700; color: var(--brand-blue);
    font-size: 56px; line-height: 60px; letter-spacing: 0.5px;
  }

  .card-stage { position: absolute; left: 0; top: 408px; width: 1200px; height: 592px; background: var(--stage); }

  .business-card {
    position: absolute; top: 516px; width: 546px; height: 306px;
    background: var(--card-bg); border-radius: 22px;
    box-shadow: 0 14px 26px rgba(0,0,0,0.18);
    overflow: hidden;
  }
  .business-card--studies { left: 40px; }
  .business-card--migration { left: 621px; width: 545px; }

  .world-map {
    position: absolute; left: 110px; top: 18px; width: 420px; height: 270px;
    background: radial-gradient(ellipse at center, var(--map-tone) 0%, rgba(227,230,238,0.5) 60%, rgba(255,255,255,0) 100%);
    border-radius: 40px;
  }

  .card-brand { position: absolute; left: 30px; top: 32px; display: flex; align-items: center; }
  .card-brand .brand-mark { width: 90px; height: 90px; }
  .card-brand .brand-name { margin-left: 18px; font-size: 25px; line-height: 27px; }

  .holder { position: absolute; right: 33px; top: 126px; text-align: right; font-size: 12.5px; line-height: 15px; }
  .holder-name { color: var(--brand-navy); font-weight: 700; font-size: 13.5px; letter-spacing: 0.5px; margin-bottom: 2px; }

  .divider { position: absolute; left: 30px; right: 33px; top: 178px; border-top: 1.5px solid var(--rule); }

  .addresses { position: absolute; left: 30px; top: 185px; font-size: 12.5px; line-height: 14px; }
  .address-label { color: var(--brand-navy); font-weight: 700; }
  .address-block + .address-block { margin-top: 8px; }

  .contacts { position: absolute; right: 33px; top: 193px; list-style: none; text-align: right; font-size: 12.5px; line-height: 17px; }
  .contacts li { display: flex; justify-content: flex-end; align-items: center; gap: 5px; }
  .contacts svg { width: 10px; height: 10px; flex: none; }
</style>
</head>
<body>

<div class="brand-lockup brand-lockup--migration">
  <div class="brand-mark"></div>
  <div class="brand-name">Brightpath<br>Migration</div>
</div>
<div class="brand-lockup brand-lockup--studies">
  <div class="brand-mark"></div>
  <div class="brand-name">Brightpath<br>Studies</div>
</div>

<div class="card-stage"></div>

<article class="business-card business-card--studies">
  <div class="world-map" role="img" aria-label="Faint world map backdrop"></div>
  <div class="card-brand"><div class="brand-mark"></div><div class="brand-name">Brightpath<br>Studies</div></div>
  <div class="holder">
    <div class="holder-name">ROSALIND TEPPERLY</div>
    <div>MARN 0719264</div>
    <div>Managing Director / Migration Agent</div>
  </div>
  <div class="divider"></div>
  <div class="addresses">
    <div class="address-block"><div class="address-label">Postal Address</div><div>PO Box 2274, Fernvale South</div><div>VIC 3195, Australia</div></div>
    <div class="address-block"><div class="address-label">Office Address</div><div>Level 1, 287 Corran Street, Tullagrove</div><div>VIC 3211</div></div>
  </div>
  <ul class="contacts">
    <li>0417296385 <svg viewBox="0 0 10 10"><rect x="2.5" y="0.5" width="5" height="9" rx="1" fill="none" stroke="#1d5a9c"/></svg></li>
    <li>61 3 8574 3162 <svg viewBox="0 0 10 10"><path d="M1 4 Q5 0 9 4 L8 5 L6.5 4 L6.5 3 Q5 2.4 3.5 3 L3.5 4 L2 5 Z M2 6 H8 V9 H2 Z" fill="#1d5a9c"/></svg></li>
    <li>+ 61 3 8539 7041 <svg viewBox="0 0 10 10"><rect x="2.5" y="1" width="5" height="3" fill="#1d5a9c"/><rect x="1" y="4" width="8" height="4" rx="1" fill="#1d5a9c"/><rect x="2.5" y="7" width="5" height="2.5" fill="#ffffff" stroke="#1d5a9c"/></svg></li>
    <li>rosalind@brightpathstudies.example <svg viewBox="0 0 10 10"><rect x="0.5" y="2" width="9" height="6.5" fill="#1d5a9c"/><path d="M0.5 2 L5 5.5 L9.5 2" fill="none" stroke="#ffffff"/></svg></li>
    <li>www.brightpathstudies.example <svg viewBox="0 0 10 10"><circle cx="5" cy="5" r="4.5" fill="#1d5a9c"/><path d="M0.5 5 H9.5 M5 0.5 V9.5" stroke="#ffffff" stroke-width="0.8"/><ellipse cx="5" cy="5" rx="2" ry="4.5" fill="none" stroke="#ffffff" stroke-width="0.8"/></svg></li>
  </ul>
</article>

<article class="business-card business-card--migration">
  <div class="world-map" role="img" aria-label="Faint world map backdrop"></div>
  <div class="card-brand"><div class="brand-mark"></div><div class="brand-name">Brightpath<br>Migration</div></div>
  <div class="holder">
    <div class="holder-name">ROSALIND TEPPERLY</div>
    <div>MARN 0719264</div>
    <div>Managing Director / Migration Agent</div>
  </div>
  <div class="divider"></div>
  <div class="addresses">
    <div class="address-block"><div class="address-label">Postal Address</div><div>PO Box 2274, Fernvale South</div><div>VIC 3195, Australia</div></div>
    <div class="address-block"><div class="address-label">Office Address</div><div>Level 1, 287 Corran Street, Tullagrove</div><div>VIC 3211</div></div>
  </div>
  <ul class="contacts">
    <li>0417296385 <svg viewBox="0 0 10 10"><rect x="2.5" y="0.5" width="5" height="9" rx="1" fill="none" stroke="#1d5a9c"/></svg></li>
    <li>61 3 8574 3162 <svg viewBox="0 0 10 10"><path d="M1 4 Q5 0 9 4 L8 5 L6.5 4 L6.5 3 Q5 2.4 3.5 3 L3.5 4 L2 5 Z M2 6 H8 V9 H2 Z" fill="#1d5a9c"/></svg></li>
    <li>+ 61 3 8539 7041 <svg viewBox="0 0 10 10"><rect x="2.5" y="1" width="5" height="3" fill="#1d5a9c"/><rect x="1" y="4" width="8" height="4" rx="1" fill="#1d5a9c"/><rect x="2.5" y="7" width="5" height="2.5" fill="#ffffff" stroke="#1d5a9c"/></svg></li>
    <li>rosalind@brightpathmigration.example <svg viewBox="0 0 10 10"><rect x="0.5" y="2" width="9" height="6.5" fill="#1d5a9c"/><path d="M0.5 2 L5 5.5 L9.5 2" fill="none" stroke="#ffffff"/></svg></li>
    <li>www.brightpathmigration.example <svg viewBox="0 0 10 10"><circle cx="5" cy="5" r="4.5" fill="#1d5a9c"/><path d="M0.5 5 H9.5 M5 0.5 V9.5" stroke="#ffffff" stroke-width="0.8"/><ellipse cx="5" cy="5" rx="2" ry="4.5" fill="none" stroke="#ffffff" stroke-width="0.8"/></svg></li>
  </ul>
</article>

</body>
</html>
```